Maple Hollow

HI We need book cover design done for a physical book. See the attached document that represents the text that we want.

The book is about retiring with financial freedom.

```html
<!DOCTYPE html>
<html lang="en">
<head>
<meta charset="utf-8">
<title>Confidence to Thrive — Book Cover</title>
<link rel="stylesheet" href="https://fonts.googleapis.com/css2?family=Bodoni+Moda:wght@400;500;600&family=Tinos:wght@400;700&display=swap">
<style>
  :root {
    --page: #ffffff;
    --ink: #121212;
    --sky-top: #dcdedb;
    --sky-mid: #d3dcdb;
    --sky-low: #c4d5d6;
    --hill-light: #e4ecec;
    --hill-blue: #a7bcc5;
    --road-blue: #6f8b9c;
    --ground: #eef2f2;
  }
  html, body {
    margin: 0;
    padding: 0;
    width: 1200px;
    height: 1200px;
    overflow: hidden;
    background: var(--page);
  }
  .book-cover {
    position: absolute;
    left: 222px;
    top: 31px;
    width: 764px;
    height: 1147px;
    background: linear-gradient(180deg, var(--sky-top) 0%, var(--sky-mid) 40%, var(--sky-low) 64%);
    box-shadow: 0 2px 8px rgba(0,0,0,0.12);
    overflow: hidden;
  }
  .cover-type {
    position: absolute;
    left: 0;
    top: 0;
    width: 764px;
    height: 736px;
  }
  .author-name {
    font-family: "Bodoni Moda", serif;
    font-weight: 400;
    font-size: 54px;
    fill: var(--ink);
  }
  .author-credit {
    font-family: "Tinos", serif;
    font-weight: 700;
    font-size: 12px;
    fill: var(--ink);
  }
  .title-word {
    font-family: "Bodoni Moda", serif;
    font-weight: 500;
    fill: var(--ink);
  }
  .title-rule {
    stroke: var(--ink);
    stroke-width: 3;
  }
  .tagline {
    font-family: "Tinos", serif;
    font-size: 31px;
    fill: var(--ink);
  }
  .cover-art {
    position: absolute;
    left: 0;
    top: 732px;
    width: 764px;
    height: 415px;
    background: linear-gradient(180deg, var(--sky-low) 0%, var(--hill-light) 22%, var(--hill-blue) 42%, var(--road-blue) 62%, var(--hill-blue) 82%, var(--ground) 100%);
  }
</style>
</head>
<body>
  <div class="book-cover">
    <svg class="cover-type" viewBox="0 0 764 736" xmlns="http://www.w3.org/2000/svg">
      <text class="author-name" x="382" y="112" text-anchor="middle" textLength="570" lengthAdjust="spacing">DANIEL WHITFORD</text>
      <text class="author-credit" x="382" y="142" text-anchor="middle" textLength="566" lengthAdjust="spacing">HOST OF THE STEADY LEDGER PODCAST AND NEXT CHAPTER HOUR</text>

      <text class="title-word" x="382" y="316" font-size="122" text-anchor="middle" textLength="633" lengthAdjust="spacingAndGlyphs">CONFIDENCE</text>
      <line class="title-rule" x1="67" y1="346" x2="326" y2="346"/>
      <text class="title-word" x="382" y="367" font-size="50" text-anchor="middle" textLength="56" lengthAdjust="spacingAndGlyphs">TO</text>
      <line class="title-rule" x1="438" y1="346" x2="699" y2="346"/>
      <text class="title-word" x="382" y="545" font-size="232" text-anchor="middle" textLength="633" lengthAdjust="spacingAndGlyphs">THRIVE</text>

      <text class="tagline" x="382" y="654" text-anchor="middle">How to Live Well When the Salary Ends</text>
      <text class="tagline" x="382" y="690" text-anchor="middle">and a New Chapter Opens</text>
    </svg>
    <div class="cover-art" role="img" aria-label="Minimal illustration of a road leading toward a rising sun between soft blue hills"></div>
  </div>
</body>
</html>
```